New Candy Packaging Design

Looking to create an attractive design for modern retail for our single stick candy that will stand out on retail shelves. It will be hung from a whole. The design should have brand elements like the irregular shapes, bright pastel colors. Please visit pebblefrostcandy.example to ensure the product could be an extension of the product range. 3 colors, pink(sakura flavor), green(muscat grape flavor), and blue(french vanilla flavor).

Target Market(s)

Millenias and Genz

Industry/Entity Type

Food

Requirements
Must have
• Look and feel of brand extension for Pebbles, Matt finish
Nice to have
• fruit shapes
Should not have
• tacky design

```html
<!DOCTYPE html>
<html lang="en">
<head>
<meta charset="utf-8">
<title>Pebbles Rock Sugar Sticks – Packaging</title>
<link rel="stylesheet" href="https://fonts.googleapis.com/css2?family=Kaushan+Script&family=Zilla+Slab:wght@400;700&display=swap">
<style>
  :root {
    --bg: #ffffff;
    --hole: #c9c9cb;
    --window: #bcbdc0;
    --ink: #141414;
    --white: #ffffff;

    --sakura-head: #e4007f;
    --sakura-deep: #7a2a86;
    --sakura-mid: #a0509c;
    --sakura-light: #f2a7cb;
    --sakura-pill: #6b2377;

    --grape-head: #cddc00;
    --grape-deep: #4f9a1e;
    --grape-mid: #8cc63f;
    --grape-light: #e4ec8a;
    --grape-pill: #3f8a19;

    --vanilla-head: #00a8e6;
    --vanilla-deep: #0a4ea3;
    --vanilla-mid: #2b86d1;
    --vanilla-light: #f3e4b8;
    --vanilla-pill: #0a4ea3;
  }

  * { box-sizing: border-box; margin: 0; padding: 0; }

  html, body {
    width: 1200px;
    height: 2271px;
    overflow: hidden;
    background: var(--bg);
  }

  .sheet {
    position: relative;
    width: 1200px;
    height: 2271px;
  }

  .pack {
    position: absolute;
    width: 307px;
    height: 836px;
    overflow: hidden;
    background: var(--head);
  }

  .pack--hero {
    left: 426px;
    top: 78px;
    transform: scale(1.137);
    transform-origin: top left;
  }
  .pack--sakura-flat { left: 81px; top: 1102px; }
  .pack--grape-flat { left: 448px; top: 1102px; }
  .pack--vanilla-flat { left: 822px; top: 1102px; }

  .pack--sakura {
    --head: var(--sakura-head);
    --deep: var(--sakura-deep);
    --mid: var(--sakura-mid);
    --light: var(--sakura-light);
    --pill: var(--sakura-pill);
  }
  .pack--grape {
    --head: var(--grape-head);
    --deep: var(--grape-deep);
    --mid: var(--grape-mid);
    --light: var(--grape-light);
    --pill: var(--grape-pill);
  }
  .pack--vanilla {
    --head: var(--vanilla-head);
    --deep: var(--vanilla-deep);
    --mid: var(--vanilla-mid);
    --light: var(--vanilla-light);
    --pill: var(--vanilla-pill);
  }

  .hang-hole {
    position: absolute;
    left: 134px;
    top: 10px;
    width: 38px;
    height: 38px;
    border-radius: 50%;
    background: var(--hole);
  }

  .seal-line {
    position: absolute;
    left: 0;
    width: 100%;
    border-top: 1.5px dashed rgba(255, 255, 255, 0.75);
  }
  .seal-line--top { top: 62px; }
  .seal-line--fold { top: 122px; }
  .seal-line--bottom { top: 790px; }

  .brand {
    position: absolute;
    left: 0;
    top: 140px;
    width: 100%;
    text-align: center;
    color: var(--white);
  }
  .brand__sub {
    display: block;
    font-family: "Zilla Slab", serif;
    font-size: 13px;
    font-weight: 400;
    letter-spacing: 0.2px;
    margin-left: 8px;
  }
  .brand__name {
    display: block;
    font-family: "Kaushan Script", cursive;
    font-size: 62px;
    line-height: 0.9;
    margin-top: -4px;
  }

  .pattern {
    position: absolute;
    left: 0;
    top: 232px;
    width: 100%;
    height: 604px;
    background:
      linear-gradient(118deg, var(--head) 0%, var(--deep) 22%, var(--light) 38%, var(--mid) 52%, var(--deep) 66%, var(--light) 80%, var(--head) 100%);
  }

  .window {
    position: absolute;
    left: 95px;
    top: 272px;
    width: 118px;
    height: 275px;
  }

  .candy-view {
    position: absolute;
    left: 103px;
    top: 282px;
    width: 102px;
    height: 255px;
    border-radius: 46px 46px 40px 40px / 30px 30px 90px 90px;
    background: linear-gradient(180deg, #f6c7cf 0%, #e8737f 50%, #f4b5bf 100%);
  }

  .flavor-art {
    position: absolute;
    border-radius: 50%;
    background: radial-gradient(circle, var(--light) 0%, var(--mid) 70%, transparent 72%);
    opacity: 0.9;
  }
  .flavor-art--upper { left: 200px; top: 490px; width: 100px; height: 100px; }
  .flavor-art--left { left: 24px; top: 612px; width: 90px; height: 90px; }
  .flavor-art--right { left: 190px; top: 640px; width: 100px; height: 100px; }

  .tagline {
    position: absolute;
    left: 0;
    top: 560px;
    width: 100%;
    font-family: "Kaushan Script", cursive;
    font-size: 44px;
    line-height: 1;
    color: var(--white);
    text-shadow:
      -2px -2px 0 var(--ink), 2px -2px 0 var(--ink),
      -2px 2px 0 var(--ink), 2px 2px 0 var(--ink),
      0 3px 0 var(--ink), 3px 0 0 var(--ink),
      -3px 0 0 var(--ink), 0 -3px 0 var(--ink);
    transform: rotate(-5deg);
  }
  .tagline__line { display: block; }
  .tagline__line--first { padding-left: 30px; }
  .tagline__line--second { padding-left: 92px; margin-top: 4px; }

  .flavor {
    position: absolute;
    left: 38px;
    top: 708px;
    font-family: "Zilla Slab", serif;
    font-weight: 700;
    font-size: 26px;
    line-height: 1.08;
    color: var(--white);
    text-shadow:
      -1.5px -1.5px 0 var(--ink), 1.5px -1.5px 0 var(--ink),
      -1.5px 1.5px 0 var(--ink), 1.5px 1.5px 0 var(--ink);
  }

  .count {
    position: absolute;
    left: 184px;
    top: 736px;
    width: 108px;
    height: 28px;
    border-radius: 14px;
    background: var(--pill);
    color: var(--white);
    font-family: "Zilla Slab", serif;
    font-weight: 700;
    font-size: 20px;
    line-height: 28px;
    text-align: center;
  }
</style>
</head>
<body>
<main class="sheet">

  <!-- Hero pouch, sakura -->
  <section class="pack pack--sakura pack--hero" aria-label="Sakura flavor pack">
    <span class="hang-hole"></span>
    <div class="brand">
      <span class="brand__sub">Rock Sugar Sticks</span>
      <span class="brand__name">Pebbles</span>
    </div>
    <div class="pattern" role="img" aria-label="Irregular pink and purple triangle pattern with dotted confetti and sakura blossoms"></div>
    <div class="candy-view" role="img" aria-label="Pink rock sugar stick seen through the clear window"></div>
    <div class="flavor-art flavor-art--upper" role="img" aria-label="Sakura blossom"></div>
    <div class="flavor-art flavor-art--left" role="img" aria-label="Sakura blossom"></div>
    <div class="flavor-art flavor-art--right" role="img" aria-label="Sakura blossom"></div>
    <p class="tagline"><span class="tagline__line tagline__line--first">A candy &amp;</span><span class="tagline__line tagline__line--second">more</span></p>
    <p class="flavor">Sakura<br>flavor</p>
    <span class="count">1 stick</span>
  </section>

  <!-- Flat dieline, sakura -->
  <section class="pack pack--sakura pack--sakura-flat" aria-label="Sakura flavor flat artwork">
    <span class="hang-hole"></span>
    <span class="seal-line seal-line--top"></span>
    <span class="seal-line seal-line--fold"></span>
    <div class="brand">
      <span class="brand__sub">Rock Sugar Sticks</span>
      <span class="brand__name">Pebbles</span>
    </div>
    <div class="pattern" role="img" aria-label="Irregular pink and purple triangle pattern with dotted confetti and sakura blossoms"></div>
    <svg class="window" viewBox="0 0 118 275" aria-hidden="true">
      <path d="M22 0 H96 Q118 0 118 24 Q116 150 88 252 Q80 275 59 275 Q38 275 30 252 Q2 150 0 24 Q0 0 22 0 Z" fill="var(--window)"/>
    </svg>
    <div class="flavor-art flavor-art--upper" role="img" aria-label="Sakura blossom"></div>
    <div class="flavor-art flavor-art--left" role="img" aria-label="Sakura blossom"></div>
    <div class="flavor-art flavor-art--right" role="img" aria-label="Sakura blossom"></div>
    <p class="tagline"><span class="tagline__line tagline__line--first">A candy &amp;</span><span class="tagline__line tagline__line--second">more</span></p>
    <p class="flavor">Sakura<br>flavor</p>
    <span class="count">1 stick</span>
    <span class="seal-line seal-line--bottom"></span>
  </section>

  <!-- Flat dieline, muscat grape -->
  <section class="pack pack--grape pack--grape-flat" aria-label="Muscat grape flavor flat artwork">
    <span class="hang-hole"></span>
    <span class="seal-line seal-line--top"></span>
    <span class="seal-line seal-line--fold"></span>
    <div class="brand">
      <span class="brand__sub">Rock Sugar Sticks</span>
      <span class="brand__name">Pebbles</span>
    </div>
    <div class="pattern" role="img" aria-label="Irregular lime and green triangle pattern with dotted confetti and muscat grape bunches"></div>
    <svg class="window" viewBox="0 0 118 275" aria-hidden="true">
      <path d="M22 0 H96 Q118 0 118 24 Q116 150 88 252 Q80 275 59 275 Q38 275 30 252 Q2 150 0 24 Q0 0 22 0 Z" fill="var(--window)"/>
    </svg>
    <div class="flavor-art flavor-art--upper" role="img" aria-label="Muscat grape bunch"></div>
    <div class="flavor-art flavor-art--left" role="img" aria-label="Muscat grape bunch"></div>
    <div class="flavor-art flavor-art--right" role="img" aria-label="Muscat grape bunch"></div>
    <p class="tagline"><span class="tagline__line tagline__line--first">A candy &amp;</span><span class="tagline__line tagline__line--second">more</span></p>
    <p class="flavor">Muscat grape<br>flavor</p>
    <span class="count">1 stick</span>
    <span class="seal-line seal-line--bottom"></span>
  </section>

  <!-- Flat dieline, french vanilla -->
  <section class="pack pack--vanilla pack--vanilla-flat" aria-label="French vanilla flavor flat artwork">
    <span class="hang-hole"></span>
    <span class="seal-line seal-line--top"></span>
    <span class="seal-line seal-line--fold"></span>
    <div class="brand">
      <span class="brand__sub">Rock Sugar Sticks</span>
      <span class="brand__name">Pebbles</span>
    </div>
    <div class="pattern" role="img" aria-label="Irregular blue and cream triangle pattern with dotted confetti and vanilla flowers with pods"></div>
    <svg class="window" viewBox="0 0 118 275" aria-hidden="true">
      <path d="M22 0 H96 Q118 0 118 24 Q116 150 88 252 Q80 275 59 275 Q38 275 30 252 Q2 150 0 24 Q0 0 22 0 Z" fill="var(--window)"/>
    </svg>
    <div class="flavor-art flavor-art--upper" role="img" aria-label="Vanilla flower and pod"></div>
    <div class="flavor-art flavor-art--left" role="img" aria-label="Vanilla flower and pod"></div>
    <div class="flavor-art flavor-art--right" role="img" aria-label="Vanilla flower and pod"></div>
    <p class="tagline"><span class="tagline__line tagline__line--first">A candy &amp;</span><span class="tagline__line tagline__line--second">more</span></p>
    <p class="flavor">French vanilla<br>flavor</p>
    <span class="count">1 stick</span>
    <span class="seal-line seal-line--bottom"></span>
  </section>

</main>
</body>
</html>
```